Mechanical Engineering Business needs a Label Design for Bottle.

We need a Label design for 2 Bottle Sizes of Cutting Paste. This is used for Machine Work Shops big and small to do applications for different cutting processes. Example : Tapping / Broaching / Drilling / Reaming / Knurling / etc. An example of a similar product can be found at https://grivolex.com/product/16-oz-grivolex-bottle/ ... https://grivolex.com/product/2-oz-grivolex-bottle/ ... Our product will be named Mil - Gel or Milling - Gel with our Company logo attached. Currently, we are open to ideas and do not have any fixed concept.

```html
<!DOCTYPE html>
<html lang="en">
<head>
<meta charset="utf-8">
<title>Milling - Gel Bottle Label</title>
<link href="https://fonts.googleapis.com/css2?family=Orbitron:wght@700&family=Red+Hat+Display:wght@500;600;700&display=swap" rel="stylesheet">
<style>
  :root {
    --maroon: #74002e;
    --maroon-dark: #5e0b2a;
    --ink: #3b2b31;
    --paper: #f7f7f7;
    --backdrop: #e4e4e6;
  }
  * { box-sizing: border-box; margin: 0; padding: 0; }
  html, body {
    width: 1200px;
    height: 1200px;
    overflow: hidden;
    background: var(--backdrop);
  }
  .canvas {
    position: relative;
    width: 1200px;
    height: 1200px;
  }
  .label {
    position: absolute;
    left: 390px;
    top: 35px;
    width: 420px;
    height: 1130px;
    background: var(--paper);
    overflow: hidden;
    font-family: "Red Hat Display", sans-serif;
  }
  .top-band {
    position: absolute;
    left: 0; top: 0;
    width: 100%;
    height: 33px;
    background: var(--maroon-dark);
  }
  .brand {
    position: absolute;
    left: 0; top: 200px;
    width: 100%;
    text-align: center;
  }
  .brand-name {
    display: inline-flex;
    align-items: center;
    gap: 12px;
    font-weight: 600;
    font-size: 42px;
    letter-spacing: 1px;
    color: var(--maroon);
    text-transform: uppercase;
  }
  .brand-dot {
    width: 20px;
    height: 20px;
    border-radius: 50%;
    background: var(--maroon);
  }
  .product-name {
    position: absolute;
    left: 18px; top: 362px;
    width: 396px;
    height: 62px;
    border: 3px solid var(--maroon);
    border-radius: 10px;
    display: flex;
    align-items: center;
    justify-content: center;
    font-family: "Orbitron", sans-serif;
    font-weight: 700;
    font-style: italic;
    font-size: 28px;
    color: var(--maroon);
    letter-spacing: 2px;
  }
  .applications {
    position: absolute;
    left: 0; top: 477px;
    width: 100%;
    text-align: center;
    color: var(--ink);
    font-weight: 600;
    font-size: 21px;
    list-style: none;
  }
  .applications-title {
    display: inline-block;
    background: var(--maroon);
    color: #fff;
    padding: 0 5px;
    line-height: 27px;
    font-size: 21px;
    margin-bottom: 10px;
  }
  .applications li {
    line-height: 38px;
  }
  .stripe {
    position: absolute;
    left: 0;
    width: 100%;
    background: var(--maroon);
  }
  .stripe-one { top: 754px; height: 24px; }
  .stripe-two { top: 784px; height: 30px; }
  .bottom-panel {
    position: absolute;
    left: 0; top: 820px;
    width: 100%;
    height: 310px;
    background: var(--maroon);
    color: #fff;
    text-align: center;
  }
  .shake-well {
    position: absolute;
    left: 0; top: 188px;
    width: 100%;
    font-weight: 700;
    font-size: 30px;
  }
  .volume {
    position: absolute;
    left: 0; top: 260px;
    width: 100%;
    font-weight: 500;
    font-size: 23px;
  }
</style>
</head>
<body>
<div class="canvas">
  <div class="label">
    <div class="top-band"></div>

    <div class="brand">
      <div class="brand-name"><span class="brand-dot"></span>Vantor Works</div>
    </div>

    <div class="product-name">MILLING - GEL</div>

    <ul class="applications">
      <li><span class="applications-title">DIFFERENT APPLICATIONS</span></li>
      <li>TAPPING</li>
      <li>BROACHING</li>
      <li>DRILLING</li>
      <li>REAMING</li>
      <li>KNURLING</li>
      <li>ETC.</li>
    </ul>

    <div class="stripe stripe-one"></div>
    <div class="stripe stripe-two"></div>

    <div class="bottom-panel">
      <div class="shake-well">SHAKE WELL</div>
      <div class="volume">16 oz / 493 ml</div>
    </div>
  </div>
</div>
</body>
</html>
```